Orlent Telecom Business Card Competition

High quality international communications for consumers and business. We are re-designing our website and re-branding. Our current (old) website can be viewed at www.goorlent-example.net Vision statement - We enable people and communities to build and maintain strong and lasting global connections This is the brand image that we are trying to get across: •Quality—Orlent delivers the highest quality connections wherever you need to communicate. •Service—Orlent is always there for you, with the industry-leading service that promises to ensure that every experience is a good one. •Value—Orlent provides the best value in the global communications market. Typical messaging: Connecting the Most Important People in the World. Focus on international communications

We want to convey our service quality and that we really care about the service we provide and our customers. We want to emphasis the international aspect of our business. We want to make it personal, but it has to relate to business as well as individuals. We want the card to be unique in design but clear enough to read. We want a business prospect as well as a regular person to look at our card and know what we do.

Target Market(s)

Consumer - multi-ethnic consumer base living in the US calling, texting and connecting with family and friends in countries around the world 2. Busine

Industry/Entity Type

Communications

Requirements
Must have
• 1. Logo must be visible (see uploaded)

2.Artist can use variations of our company colors to accent our logo:

Hex Codes:
Magenta = ab3179
Blue = 2895c0
Green = 8ebb3f

3.Must have the following slogan visible: Because Every Call Matters

below are the required data fields:

Full Name: Mark Tallow
Position: Chief Financial Officer
Office: +1 608-441-2871 ext.318
Mobile: +1 608-441-2871
Fax: +1 608-441-2871
Email: MarkT@goorlent-example.net
URL: www.goorlent-example.net
Address:
71820 Brindle Avenue
suite 412
Larkfield, OR 97163
USA

Nice to have
• Die cut cards or uniquely shaped cards would be interesting to see but not required

```html
<!DOCTYPE html>
<html lang="en">
<head>
<meta charset="utf-8">
<title>Orlent Telecom – Business Card Set</title>
<link rel="stylesheet" href="https://fonts.googleapis.com/css2?family=Open+Sans:wght@300;400;600;700&display=swap">
<style>
  :root {
    --brand-blue: #2895c0;
    --brand-magenta: #ab3179;
    --brand-green: #8ebb3f;
    --ink: #4d4d4d;
    --cut-line: #555555;
    --divider: #bcbec0;
    --paper: #ffffff;
  }
  html, body {
    margin: 0;
    padding: 0;
    width: 1200px;
    height: 1150px;
    overflow: hidden;
    background: var(--paper);
  }
  .card-sheet {
    display: block;
    width: 1200px;
    height: 1150px;
    font-family: "Open Sans", Arial, sans-serif;
  }
  .card-blue { fill: var(--brand-blue); }
  .card-white { fill: var(--paper); stroke: var(--cut-line); stroke-width: 1.6; }
  .card-edge { stroke: var(--cut-line); stroke-width: 1.6; }
  .divider { fill: var(--divider); }
  .wordmark { font-weight: 700; fill: var(--brand-blue); }
  .wordmark-dot { fill: var(--brand-magenta); }
  .contact { fill: var(--paper); font-weight: 300; }
  .contact-label { font-size: 12px; }
  .name-first { font-weight: 700; }
  .name-last { font-weight: 400; }
  .title { font-weight: 400; font-size: 12px; fill: var(--paper); }
  .slogan { font-weight: 300; font-size: 26px; fill: var(--ink); }
  .slogan-blue { fill: var(--brand-blue); }
  .slogan-magenta { fill: var(--brand-magenta); }
  .slogan-green { fill: var(--brand-green); }
  .web-address { font-weight: 400; font-size: 14px; letter-spacing: 2px; fill: var(--ink); }
</style>
</head>
<body>
<svg class="card-sheet" viewBox="0 0 1300 1245" xmlns="http://www.w3.org/2000/svg">
  <defs>
    <filter id="card-shadow" x="-10%" y="-10%" width="130%" height="140%">
      <feDropShadow dx="10" dy="12" stdDeviation="8" flood-color="#000" flood-opacity="0.45"/>
    </filter>
    <linearGradient id="texture-blue" x1="0" y1="1" x2="1" y2="0">
      <stop offset="0" stop-color="#7fc0e0" stop-opacity="0.15"/>
      <stop offset="1" stop-color="#7fc0e0" stop-opacity="0.6"/>
    </linearGradient>
    <linearGradient id="texture-pink" x1="0" y1="0" x2="1" y2="1">
      <stop offset="0" stop-color="#e0a9c7" stop-opacity="0.75"/>
      <stop offset="1" stop-color="#e0a9c7" stop-opacity="0.15"/>
    </linearGradient>
    <linearGradient id="texture-green" x1="0" y1="1" x2="1" y2="0">
      <stop offset="0" stop-color="#c5dc9c" stop-opacity="0.8"/>
      <stop offset="1" stop-color="#c5dc9c" stop-opacity="0.25"/>
    </linearGradient>
  </defs>

  <g class="card card-front-presented" filter="url(#card-shadow)">
    <rect class="card-blue" x="560" y="48" width="345" height="307"/>
    <path class="card-white" d="M373 48 H590 C650 48 680 90 680 150 V270 C680 330 640 355 580 355 H440 C400 355 373 320 373 280 Z"/>
  </g>
  <path role="img" aria-label="Soft halftone texture in light blue" fill="url(#texture-blue)"
        d="M680 255 L730 240 L790 242 L840 210 L870 190 L905 175 V355 H640 C660 330 675 300 680 255 Z"/>
  <g class="wordmark-group">
    <rect class="wordmark-dot" x="420" y="180" width="22" height="22" rx="4"/>
    <text class="wordmark" x="452" y="210" font-size="50">Orlent</text>
  </g>
  <text x="893" y="105" text-anchor="end" font-size="23" class="contact"><tspan class="name-first">Mark</tspan> <tspan class="name-last">Tallow</tspan></text>
  <text class="title" x="893" y="126" text-anchor="end">Chief Financial Officer</text>
  <text class="contact" x="893" y="150" text-anchor="end" font-size="15"><tspan class="contact-label">mobile : </tspan>+1 608-441-2871</text>
  <text class="contact" x="893" y="171" text-anchor="end" font-size="12.5"><tspan font-size="10.5">email : </tspan>MarkT@goorlent-example.net</text>

  <rect class="divider" x="215" y="432" width="850" height="11"/>

  <path class="card-white" d="M228 495 H760 V715 C740 770 710 795 675 801 H228 Z"/>
  <path role="img" aria-label="Soft halftone texture in pale magenta" fill="url(#texture-pink)"
        d="M230 497 H540 L520 530 L470 560 L400 575 L330 600 L270 628 L230 620 Z"/>
  <path role="img" aria-label="Soft halftone texture in pale green" fill="url(#texture-green)"
        d="M265 800 L270 775 L330 760 L400 740 L480 715 L560 705 L640 690 L700 675 L750 660 V720 C735 770 710 795 675 799 Z"/>
  <text class="slogan" x="493" y="652" text-anchor="middle">Because <tspan class="slogan-blue">Every</tspan> <tspan class="slogan-magenta">Call</tspan> <tspan class="slogan-green">Matters</tspan></text>
  <text class="web-address" x="493" y="682" text-anchor="middle">www.goorlent-example.net</text>

  <path class="card-white" d="M760 494 H985 C1035 494 1063 540 1063 590 V705 C1063 760 1020 799 965 799 H840 C800 799 775 775 765 740 C760 720 760 700 760 680 Z"/>
  <g class="wordmark-group">
    <rect class="wordmark-dot" x="806" y="625" width="22" height="22" rx="4"/>
    <text class="wordmark" x="838" y="655" font-size="50">Orlent</text>
  </g>

  <path class="card-blue card-edge" d="M525 833 H1058 V1140 H610 C560 1140 530 1100 525 1050 Z"/>
  <path role="img" aria-label="Soft halftone texture in light blue" fill="url(#texture-blue)"
        d="M800 1138 L805 1060 L840 1040 L900 1030 L960 1010 L1010 985 L1055 965 V1138 Z"/>
  <path class="card-white" d="M300 833 H525 V1040 C520 1100 490 1138 440 1138 H300 C250 1138 220 1100 220 1050 V920 C220 870 250 833 300 833 Z"/>
  <g class="wordmark-group">
    <rect class="wordmark-dot" x="292" y="970" width="16" height="16" rx="3"/>
    <text class="wordmark" x="316" y="992" font-size="38">Orlent</text>
  </g>
  <text x="1024" y="891" text-anchor="end" font-size="23" class="contact"><tspan class="name-first">Mark</tspan> <tspan class="name-last">Tallow</tspan></text>
  <text class="title" x="1024" y="911" text-anchor="end">Chief Financial Officer</text>
  <text class="contact" x="1024" y="937" text-anchor="end" font-size="16"><tspan class="contact-label">mobile : </tspan>+1 608-441-2871</text>
  <text class="contact" x="565" y="997" font-size="16"><tspan class="contact-label">email : </tspan>MarkT@goorlent-example.net</text>
  <text class="contact" x="565" y="1019" font-size="16"><tspan class="contact-label">office: </tspan>+1 608-441-2871 ext.318</text>
  <text class="contact" x="565" y="1042" font-size="16"><tspan class="contact-label">fax     : </tspan>+1 608-441-2871</text>
  <text class="contact" x="565" y="1065" font-size="16">71820 Brindle Avenue suite 412</text>
  <text class="contact" x="565" y="1088" font-size="16">Larkfield, OR 97163 USA</text>
</svg>
</body>
</html>
```